Looking for a "Hipster orientated" menu design for our espresso bar.
Lantern Brewhouse is part of the Marlow Kettle Group a leading Australian roasting company.
We are leaving the brief open as we don't to use any pre-conceived ideas that are in our heads. In a nutshell we don't want to be an imitation of others.
Lantern Brewhouse is an industrial inspired space with some classic elements. Coffee is our passion and simple fresh well presented food to match using the best local ingredients.

We would like our menu to have a clear distinction between beverages and food.
An open A4 size menu landscape format is ideal or perhaps folded.

This is our first crowd sourced design and the menu is a test to what will be a new webpage, online store and new brand elements for our company to the right designer.

At this stage don't worry about content i.e whats in a sandwich. Random latin under the word breakfast burger is fine.

Good luck

Target Market(s)

Hipster caffeine and food addicts

Industry/Entity Type

Industrial

Font styles to use
Decorative

Colors

Designer to choose colors to be used in the design.

Requirements
Must have
• A distinction between breakfast, lunch and beverages/coffee
Should not have
• overcrowded, hard to read

```html
<!DOCTYPE html>
<html lang="en">
<head>
<meta charset="utf-8">
<title>Lantern Brewhouse Menu</title>
<link href="https://fonts.googleapis.com/css2?family=Delius&display=swap" rel="stylesheet">
<style>
  :root {
    --chalk: #f4f4f2;
    --chalk-soft: rgba(244,244,242,0.82);
    --slate-dark: #1f1f20;
    --slate-mid: #3a3a3b;
    --blueprint-dark: #17478c;
    --blueprint-mid: #2563b2;
    --line: #ffffff;
  }
  * { box-sizing: border-box; margin: 0; padding: 0; }
  html, body { width: 849px; height: 1200px; overflow: hidden; background: #fff; }
  .sheet { width: 849px; height: 1200px; }
  .board { position: relative; width: 849px; height: 600px; overflow: hidden; color: var(--chalk); font-family: "Delius", cursive; font-weight: 400; }
  .board--slate { background: radial-gradient(ellipse at 50% 40%, var(--slate-mid) 0%, #2c2c2d 55%, var(--slate-dark) 100%); }
  .board--blueprint { background: radial-gradient(ellipse at 50% 40%, var(--blueprint-mid) 0%, #1f56a0 60%, var(--blueprint-dark) 100%); }

  .venue-name { position: absolute; left: 290px; top: 22px; width: 270px; text-align: center; font-family: "Delius", cursive; font-weight: 400; font-size: 36px; line-height: 42px; color: var(--chalk); }

  .panel { position: absolute; width: 255px; }
  .panel__frame { position: absolute; inset: 0; width: 100%; height: 100%; }
  .panel__frame path { fill: none; stroke: var(--line); vector-effect: non-scaling-stroke; }
  .panel__title { position: absolute; top: 10px; left: 0; right: 0; text-align: center; font-size: 17px; font-weight: 400; letter-spacing: 0.5px; }
  .menu-list { position: absolute; top: 40px; left: 14px; right: 12px; list-style: none; }
  .menu-item { position: relative; height: 26px; }
  .menu-item__name { display: block; font-size: 12.5px; line-height: 13px; }
  .menu-item__note { display: block; font-size: 7.5px; line-height: 9px; color: var(--chalk-soft); white-space: nowrap; }
  .menu-item__price { position: absolute; right: 0; top: 0; font-size: 12.5px; line-height: 13px; }

  .panel--coffee { left: 28px; top: 82px; height: 236px; }
  .panel--tea { left: 28px; top: 322px; height: 245px; }
  .panel--breakfast { left: 567px; top: 82px; height: 236px; }
  .panel--lunch { left: 567px; top: 332px; height: 235px; }

  .machine-drawing { position: absolute; left: 300px; top: 160px; width: 240px; height: 260px; border-radius: 6px; }
  .board--slate .machine-drawing { background: radial-gradient(ellipse, rgba(255,255,255,0.14), rgba(255,255,255,0.03) 70%); }
  .board--blueprint .machine-drawing { background: radial-gradient(ellipse, rgba(255,255,255,0.18), rgba(255,255,255,0.04) 70%); }

  .group-name { position: absolute; left: 340px; top: 490px; width: 170px; text-align: center; font-size: 14px; line-height: 18px; color: var(--chalk); }
</style>
</head>
<body>
<main class="sheet">

  <section class="board board--slate" aria-label="Lantern Brewhouse menu, chalkboard edition">
    <h1 class="venue-name">Lantern<br>Brewhouse</h1>

    <div class="panel panel--coffee">
      <svg class="panel__frame" viewBox="0 0 255 240" preserveAspectRatio="none" aria-hidden="true">
        <path stroke-width="2" d="M10,1 H245 A9,9 0 0 0 254,10 V230 A9,9 0 0 0 245,239 H10 A9,9 0 0 0 1,230 V10 A9,9 0 0 0 10,1 Z"/>
        <path stroke-width="1" d="M12,5 H243 A7,7 0 0 0 250,12 V228 A7,7 0 0 0 243,235 H12 A7,7 0 0 0 5,228 V12 A7,7 0 0 0 12,5 Z"/>
      </svg>
      <h2 class="panel__title">Coffee</h2>
      <ul class="menu-list">
        <li class="menu-item"><span class="menu-item__name">Espresso</span><span class="menu-item__note">Dolorem ipiet</span><span class="menu-item__price">$2.99</span></li>
        <li class="menu-item"><span class="menu-item__name">Cappucino</span><span class="menu-item__note">Moluptati cus sapiditam</span><span class="menu-item__price">$2.99</span></li>
        <li class="menu-item"><span class="menu-item__name">Caffe Latte</span><span class="menu-item__note">Eos cuscil magniscid magnatur</span><span class="menu-item__price">$2.99</span></li>
        <li class="menu-item"><span class="menu-item__name">Caffe Mocha</span><span class="menu-item__note">Volut lam volorpo</span><span class="menu-item__price">$2.99</span></li>
        <li class="menu-item"><span class="menu-item__name">Macchiato</span><span class="menu-item__note">Nam as et de nit eos et rem atatur,</span><span class="menu-item__price">$2.99</span></li>
        <li class="menu-item"><span class="menu-item__name">House Coffee</span><span class="menu-item__note">Bernati orernat et</span><span class="menu-item__price">$2.99</span></li>
        <li class="menu-item"><span class="menu-item__name">Caffe Americano</span><span class="menu-item__note">sequatis autatus</span><span class="menu-item__price">$2.99</span></li>
      </ul>
    </div>

    <div class="panel panel--tea">
      <svg class="panel__frame" viewBox="0 0 255 240" preserveAspectRatio="none" aria-hidden="true">
        <path stroke-width="2" d="M10,1 H245 A9,9 0 0 0 254,10 V230 A9,9 0 0 0 245,239 H10 A9,9 0 0 0 1,230 V10 A9,9 0 0 0 10,1 Z"/>
        <path stroke-width="1" d="M12,5 H243 A7,7 0 0 0 250,12 V228 A7,7 0 0 0 243,235 H12 A7,7 0 0 0 5,228 V12 A7,7 0 0 0 12,5 Z"/>
      </svg>
      <h2 class="panel__title">Tea</h2>
      <ul class="menu-list">
        <li class="menu-item"><span class="menu-item__name">Delendis Quis Molorib</span><span class="menu-item__note">Usandene doluptate erorum</span><span class="menu-item__price">$2.99</span></li>
        <li class="menu-item"><span class="menu-item__name">Core Nulpa</span><span class="menu-item__note">Cum ressereribus excea est omnis</span><span class="menu-item__price">$2.99</span></li>
        <li class="menu-item"><span class="menu-item__name">Aut Et Venimodit</span><span class="menu-item__note">Optatio reptati omnis sitatqui</span><span class="menu-item__price">$2.99</span></li>
        <li class="menu-item"><span class="menu-item__name">Vercimusciis Illa</span><span class="menu-item__note">Nes nimi, sequatis autatust</span><span class="menu-item__price">$2.99</span></li>
        <li class="menu-item"><span class="menu-item__name">Que Nobitatqui</span><span class="menu-item__note">Sequame ndebis aped es aut</span><span class="menu-item__price">$2.99</span></li>
        <li class="menu-item"><span class="menu-item__name">Quistin Pernam</span><span class="menu-item__note">Qui odicia veliquam eritas que</span><span class="menu-item__price">$2.99</span></li>
        <li class="menu-item"><span class="menu-item__name">Vercimusciis Illa</span><span class="menu-item__note">Nes nimi, sequatis autatust</span><span class="menu-item__price">$2.99</span></li>
      </ul>
    </div>

    <div class="panel panel--breakfast">
      <svg class="panel__frame" viewBox="0 0 255 240" preserveAspectRatio="none" aria-hidden="true">
        <path stroke-width="2" d="M10,1 H245 A9,9 0 0 0 254,10 V230 A9,9 0 0 0 245,239 H10 A9,9 0 0 0 1,230 V10 A9,9 0 0 0 10,1 Z"/>
        <path stroke-width="1" d="M12,5 H243 A7,7 0 0 0 250,12 V228 A7,7 0 0 0 243,235 H12 A7,7 0 0 0 5,228 V12 A7,7 0 0 0 12,5 Z"/>
      </svg>
      <h2 class="panel__title">Breakfast</h2>
      <ul class="menu-list">
        <li class="menu-item"><span class="menu-item__name">Mincimagnis Que</span><span class="menu-item__note">Odilassint as maximus</span><span class="menu-item__price">$2.99</span></li>
        <li class="menu-item"><span class="menu-item__name">Antoressit Versperi</span><span class="menu-item__note">Doluptatius volore</span><span class="menu-item__price">$2.99</span></li>
        <li class="menu-item"><span class="menu-item__name">Nos As Sum Ad Quam</span><span class="menu-item__note">Consecae pro occus moluptaquos</span><span class="menu-item__price">$2.99</span></li>
        <li class="menu-item"><span class="menu-item__name">Veligent Qui Blatiumquas</span><span class="menu-item__note">Dolorem ipiet acepero con</span><span class="menu-item__price">$2.99</span></li>
        <li class="menu-item"><span class="menu-item__name">Comnim Facerum Hil Esto</span><span class="menu-item__note">Voluptatusam qui aut</span><span class="menu-item__price">$2.99</span></li>
        <li class="menu-item"><span class="menu-item__name">Vendam Nat Aspictur</span><span class="menu-item__note">Quistis in num inihit landist</span><span class="menu-item__price">$2.99</span></li>
        <li class="menu-item"><span class="menu-item__name">Aut Et Venimodit</span><span class="menu-item__note">Optatio reptati omnis sitatqui</span><span class="menu-item__price">$2.99</span></li>
      </ul>
    </div>

    <div class="panel panel--lunch">
      <svg class="panel__frame" viewBox="0 0 255 240" preserveAspectRatio="none" aria-hidden="true">
        <path stroke-width="2" d="M10,1 H245 A9,9 0 0 0 254,10 V230 A9,9 0 0 0 245,239 H10 A9,9 0 0 0 1,230 V10 A9,9 0 0 0 10,1 Z"/>
        <path stroke-width="1" d="M12,5 H243 A7,7 0 0 0 250,12 V228 A7,7 0 0 0 243,235 H12 A7,7 0 0 0 5,228 V12 A7,7 0 0 0 12,5 Z"/>
      </svg>
      <h2 class="panel__title">Lunch</h2>
      <ul class="menu-list">
        <li class="menu-item"><span class="menu-item__name">Quaepuda Nobit</span><span class="menu-item__note">Eos Autem Acesed Elecupt Atectur</span><span class="menu-item__price">$2.99</span></li>
        <li class="menu-item"><span class="menu-item__name">Eratect Empedistiam</span><span class="menu-item__note">Juntusc Picipiet Evenimusae Inciatia</span><span class="menu-item__price">$2.99</span></li>
        <li class="menu-item"><span class="menu-item__name">Quam Et Laut</span><span class="menu-item__note">Inciusa Pellaut Quam Quiatat Uribusa</span><span class="menu-item__price">$2.99</span></li>
        <li class="menu-item"><span class="menu-item__name">Peliquasped Quam, Officiet</span><span class="menu-item__note">Pro Volo Et Rectem Et</span><span class="menu-item__price">$2.99</span></li>
        <li class="menu-item"><span class="menu-item__name">Quundis Ipsanis</span><span class="menu-item__note">Custis Non Nusa Quo Core</span><span class="menu-item__price">$2.99</span></li>
        <li class="menu-item"><span class="menu-item__name">Quam Et Laut</span><span class="menu-item__note">Inciusa Pellaut Quam Uribusa</span><span class="menu-item__price">$2.99</span></li>
        <li class="menu-item"><span class="menu-item__name">Core Nulpa</span><span class="menu-item__note">Cum ressereribus excea omnis</span><span class="menu-item__price">$2.99</span></li>
      </ul>
    </div>

    <div class="machine-drawing" role="img" aria-label="White-line patent-style technical drawing of a lever espresso machine pouring into a jug, with numbered callouts"></div>
    <p class="group-name">Marlow Kettle Group</p>
  </section>

  <section class="board board--blueprint" aria-label="Lantern Brewhouse menu, blueprint edition">
    <h1 class="venue-name">Lantern<br>Brewhouse</h1>

    <div class="panel panel--coffee">
      <svg class="panel__frame" viewBox="0 0 255 240" preserveAspectRatio="none" aria-hidden="true">
        <path stroke-width="2" d="M10,1 H245 A9,9 0 0 0 254,10 V230 A9,9 0 0 0 245,239 H10 A9,9 0 0 0 1,230 V10 A9,9 0 0 0 10,1 Z"/>
        <path stroke-width="1" d="M12,5 H243 A7,7 0 0 0 250,12 V228 A7,7 0 0 0 243,235 H12 A7,7 0 0 0 5,228 V12 A7,7 0 0 0 12,5 Z"/>
      </svg>
      <h2 class="panel__title">Coffee</h2>
      <ul class="menu-list">
        <li class="menu-item"><span class="menu-item__name">Espresso</span><span class="menu-item__note">Dolorem ipiet</span><span class="menu-item__price">$2.99</span></li>
        <li class="menu-item"><span class="menu-item__name">Cappucino</span><span class="menu-item__note">Moluptati cus sapiditam</span><span class="menu-item__price">$2.99</span></li>
        <li class="menu-item"><span class="menu-item__name">Caffe Latte</span><span class="menu-item__note">Eos cuscil magniscid magnatur</span><span class="menu-item__price">$2.99</span></li>
        <li class="menu-item"><span class="menu-item__name">Caffe Mocha</span><span class="menu-item__note">Volut lam volorpo</span><span class="menu-item__price">$2.99</span></li>
        <li class="menu-item"><span class="menu-item__name">Macchiato</span><span class="menu-item__note">Nam as et de nit eos et rem atatur,</span><span class="menu-item__price">$2.99</span></li>
        <li class="menu-item"><span class="menu-item__name">House Coffee</span><span class="menu-item__note">Bernati orernat et</span><span class="menu-item__price">$2.99</span></li>
        <li class="menu-item"><span class="menu-item__name">Caffe Americano</span><span class="menu-item__note">sequatis autatus</span><span class="menu-item__price">$2.99</span></li>
      </ul>
    </div>

    <div class="panel panel--tea">
      <svg class="panel__frame" viewBox="0 0 255 240" preserveAspectRatio="none" aria-hidden="true">
        <path stroke-width="2" d="M10,1 H245 A9,9 0 0 0 254,10 V230 A9,9 0 0 0 245,239 H10 A9,9 0 0 0 1,230 V10 A9,9 0 0 0 10,1 Z"/>
        <path stroke-width="1" d="M12,5 H243 A7,7 0 0 0 250,12 V228 A7,7 0 0 0 243,235 H12 A7,7 0 0 0 5,228 V12 A7,7 0 0 0 12,5 Z"/>
      </svg>
      <h2 class="panel__title">Tea</h2>
      <ul class="menu-list">
        <li class="menu-item"><span class="menu-item__name">Delendis Quis Molorib</span><span class="menu-item__note">Usandene doluptate erorum</span><span class="menu-item__price">$2.99</span></li>
        <li class="menu-item"><span class="menu-item__name">Core Nulpa</span><span class="menu-item__note">Cum ressereribus excea est omnis</span><span class="menu-item__price">$2.99</span></li>
        <li class="menu-item"><span class="menu-item__name">Aut Et Venimodit</span><span class="menu-item__note">Optatio reptati omnis sitatqui</span><span class="menu-item__price">$2.99</span></li>
        <li class="menu-item"><span class="menu-item__name">Vercimusciis Illa</span><span class="menu-item__note">Nes nimi, sequatis autatust</span><span class="menu-item__price">$2.99</span></li>
        <li class="menu-item"><span class="menu-item__name">Que Nobitatqui</span><span class="menu-item__note">Sequame ndebis aped es aut</span><span class="menu-item__price">$2.99</span></li>
        <li class="menu-item"><span class="menu-item__name">Quistin Pernam</span><span class="menu-item__note">Qui odicia veliquam eritas que</span><span class="menu-item__price">$2.99</span></li>
        <li class="menu-item"><span class="menu-item__name">Vercimusciis Illa</span><span class="menu-item__note">Nes nimi, sequatis autatust</span><span class="menu-item__price">$2.99</span></li>
      </ul>
    </div>

    <div class="panel panel--breakfast">
      <svg class="panel__frame" viewBox="0 0 255 240" preserveAspectRatio="none" aria-hidden="true">
        <path stroke-width="2" d="M10,1 H245 A9,9 0 0 0 254,10 V230 A9,9 0 0 0 245,239 H10 A9,9 0 0 0 1,230 V10 A9,9 0 0 0 10,1 Z"/>
        <path stroke-width="1" d="M12,5 H243 A7,7 0 0 0 250,12 V228 A7,7 0 0 0 243,235 H12 A7,7 0 0 0 5,228 V12 A7,7 0 0 0 12,5 Z"/>
      </svg>
      <h2 class="panel__title">Breakfast</h2>
      <ul class="menu-list">
        <li class="menu-item"><span class="menu-item__name">Mincimagnis Que</span><span class="menu-item__note">Odilassint as maximus</span><span class="menu-item__price">$2.99</span></li>
        <li class="menu-item"><span class="menu-item__name">Antoressit Versperi</span><span class="menu-item__note">Doluptatius volore</span><span class="menu-item__price">$2.99</span></li>
        <li class="menu-item"><span class="menu-item__name">Nos As Sum Ad Quam</span><span class="menu-item__note">Consecae pro occus moluptaquos</span><span class="menu-item__price">$2.99</span></li>
        <li class="menu-item"><span class="menu-item__name">Veligent Qui Blatiumquas</span><span class="menu-item__note">Dolorem ipiet acepero con</span><span class="menu-item__price">$2.99</span></li>
        <li class="menu-item"><span class="menu-item__name">Comnim Facerum Hil Esto</span><span class="menu-item__note">Voluptatusam qui aut</span><span class="menu-item__price">$2.99</span></li>
        <li class="menu-item"><span class="menu-item__name">Vendam Nat Aspictur</span><span class="menu-item__note">Quistis in num inihit landist</span><span class="menu-item__price">$2.99</span></li>
        <li class="menu-item"><span class="menu-item__name">Aut Et Venimodit</span><span class="menu-item__note">Optatio reptati omnis sitatqui</span><span class="menu-item__price">$2.99</span></li>
      </ul>
    </div>

    <div class="panel panel--lunch">
      <svg class="panel__frame" viewBox="0 0 255 240" preserveAspectRatio="none" aria-hidden="true">
        <path stroke-width="2" d="M10,1 H245 A9,9 0 0 0 254,10 V230 A9,9 0 0 0 245,239 H10 A9,9 0 0 0 1,230 V10 A9,9 0 0 0 10,1 Z"/>
        <path stroke-width="1" d="M12,5 H243 A7,7 0 0 0 250,12 V228 A7,7 0 0 0 243,235 H12 A7,7 0 0 0 5,228 V12 A7,7 0 0 0 12,5 Z"/>
      </svg>
      <h2 class="panel__title">Lunch</h2>
      <ul class="menu-list">
        <li class="menu-item"><span class="menu-item__name">Quaepuda Nobit</span><span class="menu-item__note">Eos Autem Acesed Elecupt Atectur</span><span class="menu-item__price">$2.99</span></li>
        <li class="menu-item"><span class="menu-item__name">Eratect Empedistiam</span><span class="menu-item__note">Juntusc Picipiet Evenimusae Inciatia</span><span class="menu-item__price">$2.99</span></li>
        <li class="menu-item"><span class="menu-item__name">Quam Et Laut</span><span class="menu-item__note">Inciusa Pellaut Quam Quiatat Uribusa</span><span class="menu-item__price">$2.99</span></li>
        <li class="menu-item"><span class="menu-item__name">Peliquasped Quam, Officiet</span><span class="menu-item__note">Pro Volo Et Rectem Et</span><span class="menu-item__price">$2.99</span></li>
        <li class="menu-item"><span class="menu-item__name">Quundis Ipsanis</span><span class="menu-item__note">Custis Non Nusa Quo Core</span><span class="menu-item__price">$2.99</span></li>
        <li class="menu-item"><span class="menu-item__name">Quam Et Laut</span><span class="menu-item__note">Inciusa Pellaut Quam Uribusa</span><span class="menu-item__price">$2.99</span></li>
        <li class="menu-item"><span class="menu-item__name">Core Nulpa</span><span class="menu-item__note">Cum ressereribus excea omnis</span><span class="menu-item__price">$2.99</span></li>
      </ul>
    </div>

    <div class="machine-drawing" role="img" aria-label="White-line patent-style technical drawing of a lever espresso machine pouring into a jug, with numbered callouts"></div>
    <p class="group-name">Marlow Kettle Group</p>
  </section>

</main>
</body>
</html>
```